Real Estate Agent Business Card Needs a New Eye Catching Design

Looking for a designer that can revamp a current business card.
Looking for something with a lot more style.
Something that will catch the eye

Included in the file:
The old business card. (Old Business Card)
A new place holder image to be used as headshot. (Temp Headshot)
Homevane KT Logo (KT logo)
Fair Dwelling Access Logo (AC logo)

The working PSD file will need to be delivered with the individual layers separated and edible. (I'll being changing the new headshot later)
Any fonts used also need to be delivered.

Overall, the old business card has the elements but in a horrible state.
If you have any questions, please feel free to reach out.

Thank you

Glen

Target Market(s)

Individuals want to either sale or buy a home

Industry/Entity Type

Real Estate Agent

Design Requirements:
Headshot needs to be a head and shoulders and have a transparent background.

The American Flag should implemented into the design somehow.

Both the KT logo and AC logo need to be incorporated.

All information on the OLD Business Card should be included.

Requirements
Must have
• Transparent head shot set against the final background
• American Flag and/or colors-theme incorporated
• KT logo and AC logo incorporated

```html
<!DOCTYPE html>
<html lang="en">
<head>
<meta charset="utf-8">
<title>Bright Peak Realty – Business Card</title>
<link rel="stylesheet" href="https://fonts.googleapis.com/css2?family=Jost:wght@400&family=Roboto:wght@400;500;700&display=swap">
<style>
  :root {
    --bg: #6f7479;
    --card: #ffffff;
    --accent: #d47c66;
    --ink: #3a3a3a;
    --body: #4a4a4a;
    --flag-blue: #363a7a;
    --flag-red: #d8132a;
    --photo-dark: #3b3434;
    --photo-light: #ddd6d2;
  }
  * { margin: 0; padding: 0; box-sizing: border-box; }
  html, body { width: 1200px; height: 801px; overflow: hidden; background: var(--bg); }
  .card {
    position: absolute; left: 75px; top: 100px; width: 1050px; height: 600px;
    background: var(--card); overflow: hidden;
    font-family: "Roboto", Arial, sans-serif;
  }
  .company {
    position: absolute; left: 90px; top: 70px;
    font-family: "Jost", "Futura", sans-serif; font-weight: 400;
    font-size: 60px; letter-spacing: 1px; color: var(--accent);
  }
  .agent-name {
    position: absolute; left: 92px; top: 200px;
    font-weight: 700; font-size: 44px; color: var(--accent);
  }
  .agent-title {
    position: absolute; left: 94px; top: 254px;
    font-weight: 500; font-size: 30px; color: var(--ink); letter-spacing: 0.5px;
  }
  .address {
    position: absolute; left: 96px; top: 305px;
    font-size: 28px; line-height: 34px; color: var(--body);
  }
  .contacts { position: absolute; left: 96px; top: 390px; list-style: none; }
  .contacts li {
    display: flex; align-items: center; gap: 14px;
    font-size: 28px; line-height: 35px; color: var(--body);
  }
  .contacts svg { width: 24px; height: 24px; fill: var(--accent); flex: none; }
  .headshot {
    position: absolute; left: 790px; top: 95px; width: 210px; height: 250px;
    border: 1.5px solid #8a8a8a; border-radius: 22px;
    background: linear-gradient(180deg, var(--photo-light) 0%, var(--photo-light) 45%, var(--photo-dark) 70%);
  }
  .badges {
    position: absolute; left: 770px; top: 385px;
    display: flex; align-items: center; gap: 18px;
  }
  .badge { display: flex; align-items: center; gap: 6px; font-size: 15px; font-weight: 700; color: #111; }
  .badge-mark { width: 26px; height: 26px; border: 2px solid #111; }
  .flag-band { position: absolute; bottom: 0; }
  .flag-blue { left: 0; width: 500px; height: 72px; background: var(--flag-blue); }
  .flag-red { left: 500px; width: 550px; height: 46px; background: var(--flag-red); }
  .flag-blue svg { position: absolute; left: 0; top: 0; width: 500px; height: 72px; fill: #fff; }
</style>
</head>
<body>
<main class="card">
  <h1 class="company">BRIGHT PEAK REALTY</h1>
  <h2 class="agent-name">Dana Whitfield</h2>
  <p class="agent-title">HOMEVANE</p>
  <p class="address">2710 N. Ridge Road<br>Carlow, NV 89310</p>
  <ul class="contacts">
    <li><svg viewBox="0 0 24 24"><path d="M6.6 10.8a15 15 0 0 0 6.6 6.6l2.2-2.2c.3-.3.7-.4 1-.2 1.1.4 2.3.6 3.6.6.6 0 1 .4 1 1V20c0 .6-.4 1-1 1A17 17 0 0 1 3 4c0-.6.4-1 1-1h3.5c.6 0 1 .4 1 1 0 1.3.2 2.5.6 3.6.1.3 0 .7-.2 1z"/></svg>555 - 014 - 2287</li>
    <li><svg viewBox="0 0 24 24"><path d="M7 1h10a2 2 0 0 1 2 2v18a2 2 0 0 1-2 2H7a2 2 0 0 1-2-2V3a2 2 0 0 1 2-2zm0 3v14h10V4zm5 15.5a1 1 0 1 0 0 2 1 1 0 0 0 0-2z"/></svg>555-016-4410</li>
    <li><svg viewBox="0 0 24 24"><path d="M7 2h8l3 3v4H7zM4 10h16a2 2 0 0 1 2 2v6H2v-6a2 2 0 0 1 2-2zm3 9h10v3H7z"/></svg>555-016-4419</li>
    <li><svg viewBox="0 0 24 24"><path d="M2 5h20v14H2zm2 2v.5l8 5.5 8-5.5V7z"/></svg>sales@brightpeakhomes.com</li>
    <li><svg viewBox="0 0 24 24"><path d="M12 2a10 10 0 1 0 0 20 10 10 0 0 0 0-20zm-1 3c-1 1-3 1-4 3s1 3 2 3 1 2 2 3-1 3 0 4c-4-.5-7-4-7-7.5C4 7 7 5 11 5zm3 1c3 1 5 3.5 5 6.5 0 1-.3 2-.7 3-1-.5-1-2-2-2.5s-2 0-2.5-1 1-2 .5-3-1-1.5-.3-3z"/></svg>www.brightpeakhomes.com</li>
  </ul>
  <div class="headshot" role="img" aria-label="Agent headshot, head and shoulders on transparent background"></div>
  <div class="badges">
    <div class="badge"><span class="badge-mark"></span>Homevane KT</div>
    <div class="badge"><span class="badge-mark"></span>Fair Dwelling Access</div>
  </div>
  <div class="flag-band flag-blue">
    <svg viewBox="0 0 500 72" aria-hidden="true">
      <defs><path id="star" d="M0-17 4-5.5 16-5.5 6.5 1.8 10 13.5 0 6.5-10 13.5-6.5 1.8-16-5.5-4-5.5z"/></defs>
      <use href="#star" x="45" y="38"/><use href="#star" x="130" y="38"/><use href="#star" x="215" y="38"/>
      <use href="#star" x="300" y="38"/><use href="#star" x="385" y="38"/><use href="#star" x="465" y="38"/>
    </svg>
  </div>
  <div class="flag-band flag-red"></div>
</main>
</body>
</html>
```